M&A Advisory firm needs elegant and powerful letterhead

We need a powerful but elegant letterhead to engage with the international financial industry.

Target Market(s)

New York and International Financial Industry

Industry/Entity Type

Finance

Font styles to use
Other font styles liked:
• Poppins

Requirements
Must have
• 482 W 71st Street 14th Floor New York, NY 10157 O: +1 (212) 555 0147 F: +1 (212) 555 0182

```html
<!DOCTYPE html>
<html lang="en">
<head>
<meta charset="utf-8">
<title>Halden Letterhead</title>
<link href="https://fonts.googleapis.com/css2?family=Poppins:wght@400;500&family=Questrial&display=swap" rel="stylesheet">
<style>
  :root {
    --brand-blue: #134f91;
    --band-grey: #808184;
    --paper-light: #e4e4e4;
    --paper-dark: #d2d2d3;
    --ink: #4a4a4c;
    --mark-tint: rgba(160, 170, 190, 0.22);
    --white: #ffffff;
  }
  * { margin: 0; padding: 0; box-sizing: border-box; }
  html, body { width: 1023px; height: 1200px; overflow: hidden; }
  body { background: var(--paper-dark); }
  .letterhead {
    position: relative;
    width: 1023px;
    height: 1200px;
    background: linear-gradient(90deg, var(--paper-light) 0%, var(--paper-dark) 100%);
    font-family: "Questrial", sans-serif;
    color: var(--ink);
    overflow: hidden;
  }
  .brand {
    position: absolute;
    left: 102px;
    top: 96px;
    display: flex;
    align-items: center;
    gap: 16px;
  }
  .brand-dot {
    width: 40px; height: 40px;
    border-radius: 50%;
    background: var(--brand-blue);
  }
  .brand-name {
    font-family: "Poppins", sans-serif;
    font-weight: 500;
    font-size: 48px;
    letter-spacing: 1px;
    line-height: 1;
    color: var(--brand-blue);
  }
  .brand-tagline {
    font-family: "Poppins", sans-serif;
    font-weight: 500;
    font-size: 12px;
    letter-spacing: 3px;
    color: var(--brand-blue);
    margin-top: 4px;
  }
  .backdrop-mark {
    position: absolute;
    left: 330px; top: 420px;
    width: 360px; height: 360px;
  }
  .letter-body {
    position: absolute;
    left: 97px;
    width: 843px;
    font-size: 14.6px;
    line-height: 18.2px;
    text-align: justify;
  }
  .salutation { top: 314px; font-size: 18px; line-height: 24px; }
  .para-1 { top: 379px; }
  .para-2 { top: 471px; }
  .para-3 { top: 580px; }
  .closing { top: 810px; font-size: 14.6px; }
  .footer-band {
    position: absolute;
    left: 0; top: 1093px;
    width: 1023px; height: 30px;
    display: flex;
  }
  .footer-main {
    width: 887px;
    background: var(--brand-blue);
    color: var(--white);
    font-family: "Poppins", sans-serif;
    font-size: 13.5px;
    display: flex;
    align-items: center;
    padding-left: 80px;
    gap: 24px;
    white-space: nowrap;
  }
  .contact { display: flex; align-items: center; gap: 6px; }
  .contact svg { width: 18px; height: 18px; }
  .footer-end { flex: 1; background: var(--band-grey); position: relative; }
  .footer-dot {
    position: absolute;
    left: -20px; top: -4px;
    width: 38px; height: 38px;
    border-radius: 50%;
    background: var(--brand-blue);
    border: 3px solid var(--white);
  }
</style>
</head>
<body>
<main class="letterhead">
  <header class="brand">
    <div class="brand-dot"></div>
    <div>
      <div class="brand-name">HALDEN</div>
      <div class="brand-tagline">Advisory Partners</div>
    </div>
  </header>

  <svg class="backdrop-mark" viewBox="0 0 360 360" aria-hidden="true">
    <circle cx="180" cy="180" r="175" fill="var(--mark-tint)"/>
  </svg>

  <p class="letter-body salutation">Dear Daniel,</p>

  <p class="letter-body para-1">Donec malesuada orci vitae nulla accumsan porta a id massa. Quisque accumsan iaculis magna sit amet fringilla. Maecenas consequat, magna eget tincidunt semper, odio nibh rutrum mi, id feugiat ante nisi eu risus. Vestibulum nunc orci, rhoncus a placerat in, ultricies in mi. Cras mattis varius eros, vel fringilla nisi suscipit eget. Quisque scelerisque sagittis nulla at porttitor.</p>

  <p class="letter-body para-2">Lorem ipsum dolor sit amet, consectetur adipiscing elit. Donec orci purus, luctus vitae dignissim eu, iaculis sed purus. Vivamus faucibus, ipsum nec aliquet viverra, leo mauris condimentum ligula, sit amet sagittis enim ligula quis arcu. Nam egestas tortor id nisi porttitor mattis. In tortor ante, ultricies in suscipit a, tempus non massa. Vivamus et auctor mi. Fusce vel massa nulla. Phasellus nec eros mauris, et scelerisque orci.</p>

  <p class="letter-body para-3">It is a long established fact that a reader will be distracted by the readable content of a page when looking at its layout. The point of using Lorem Ipsum is that it has a more-or-less normal distribution of letters, as opposed to using 'Content here, content here', making it look like readable English. Many desktop publishing packages<br>t<br>Sed id augue vitae urna euismod commodo aliquet a quam. Pellentesque arcu velit, cursus et malesuada ut, consequat et diam. Nullam erat sem, rhoncus id ullamcorper vitae, rhoncus et arcu. In ultricies ultricies nulla, ut rutrum nisi iaculis at. Donec eu magna a metus ornare faucibus. Fusce aliquet faucibus ultricies. Morbi semper, est id tincidunt gravida, sem arcu adipiscing lacus, ac bibendum nulla leo eu purus. Quisque nec diam sed risus consectetur a ccumsan quis quis nibh. Vestibulum id purus lorem.</p>

  <p class="letter-body closing">Sincerely,</p>

  <footer class="footer-band">
    <div class="footer-main">
      <span class="address">482 W 71st Street 14th Floor, New York, NY 10157</span>
      <span class="contact">
        <svg viewBox="0 0 18 18" aria-hidden="true"><circle cx="9" cy="9" r="9" fill="#fff"/><path d="M6 4.5l2 2-1 1.2c.6 1.3 1.5 2.2 2.8 2.8l1.2-1 2 2-1.2 1.5C8.6 12.8 5.2 9.4 4.5 6.2z" fill="#134f91"/></svg>
        +1 (212) 555 0147
      </span>
      <span class="contact">
        <svg viewBox="0 0 18 18" aria-hidden="true"><circle cx="9" cy="9" r="9" fill="#fff"/><rect x="5.5" y="4.5" width="7" height="3" fill="#134f91"/><rect x="4.5" y="7.5" width="9" height="4.5" rx="1" fill="#134f91"/><rect x="6" y="10.5" width="6" height="3" fill="#134f91"/></svg>
        +1 (212) 555 0182
      </span>
    </div>
    <div class="footer-end"><div class="footer-dot"></div></div>
  </footer>
</main>
</body>
</html>
```